Fenwick Creek Rodeo Sponsor Brochure/letter

We are wanting a professional looking brochure/letter that can be given to potential sponsors. This can be multiple pages the last page needs to be the Invoice (attached example) the prices on the example can be used.. this is a first nation rodeo and we are looking for sponsorship I can provide more photos if needed

Target Market(s)

This will be local corporate business's so this needs to be very professional looking

Industry/Entity Type

This is an event but we are looking for cooperate sponsorship

Font styles to use
Serif

Colors
0054AA
0677BA
7BADD7
CADEEF
E8F1F8
FFC000
F8CF3A
FAE287
FDF2CF
FEFAEE
F0912C
F2A743
F7CA91
FBE8D2
FDF5EE
EB3D1F
EC4F4E
F09395
F8D3D4
FCEDEE

Requirements
Must have
• The basic information, must have some quotes and photos can be multiple pages
Nice to have
• I would like to see that it is interactive, but gets to the point
Should not have
• no cartoon or must not look cheap

```html
<!DOCTYPE html>
<html lang="en">
<head>
<meta charset="utf-8">
<title>Fenwick Creek Rodeo – Sponsorship Proposal</title>
<link href="https://fonts.googleapis.com/css2?family=Anton&family=Montserrat:wght@600;700;800&family=Poppins:wght@400;500;600;700&display=swap" rel="stylesheet">
<style>
:root{
  --backdrop:#b9b9b9;
  --paper:#ffffff;
  --brown:#3b220d;
  --brown-text:#6a3812;
  --blue:#1d5a86;
  --blue-dark:#17476b;
  --green:#8cb526;
  --pale:#e6eef3;
  --ink:#222;
  --muted:#555;
  --gold:#c9a418;
  --bronze:#a86a25;
  --orange:#f0912c;
  --red:#e2261f;
}
*{margin:0;padding:0;box-sizing:border-box}
html,body{width:1200px;height:2302px;overflow:hidden}
body{background:var(--backdrop);font-family:'Poppins',sans-serif;color:var(--ink);position:relative}
.page{position:absolute;width:493px;height:639px;background:var(--paper);overflow:hidden}
.abs{position:absolute}
.url{position:absolute;font-family:'Poppins',sans-serif;font-size:10.5px;letter-spacing:2.6px;color:#222}
.url b{font-weight:700}
.pnum{display:inline-block;width:11px;height:11px;border-radius:50%;background:#dde6ee;font-size:6.5px;letter-spacing:0;text-align:center;line-height:11px;margin-left:6px;vertical-align:middle;color:var(--blue)}
.brand{position:absolute;display:flex;align-items:center;gap:7px;font-family:'Poppins',sans-serif;font-weight:600;color:#2b2b2b;line-height:1.05}
.brand .dot{width:26px;height:26px;border-radius:50%;background:var(--green);flex:none}
.brand .name{font-size:15px}
.brand .sub{font-size:8.5px;font-weight:600}
.photo{position:absolute}
h2.section{font-family:'Montserrat',sans-serif;font-weight:800;line-height:.9;position:absolute}
h2.section .top{color:var(--brown-text);display:block}
h2.section .bot{color:var(--blue);display:block}

/* page 1 */
.cover-band{position:absolute;left:0;top:288px;width:493px;height:351px;background:var(--brown)}
.cover-title{position:absolute;left:0;width:493px;text-align:center;top:498px;font-family:'Anton',sans-serif;font-size:52px;color:#fff;letter-spacing:.5px;line-height:1}
.cover-sub{position:absolute;left:0;width:493px;text-align:center;top:547px;font-family:'Montserrat',sans-serif;font-weight:800;font-size:32px;color:var(--green);letter-spacing:11px;line-height:1}
.cover-url{left:0;width:493px;text-align:center;top:590px;color:#fff;font-size:12px}

/* page 2 */
.quote-mark{position:absolute;left:4px;top:-38px;font-family:'Montserrat',sans-serif;font-weight:800;font-size:190px;color:#a8bac9;line-height:1}
.quote-ghost{position:absolute;right:-6px;top:-30px;font-family:'Montserrat',sans-serif;font-weight:800;font-size:230px;color:#eef1f4;line-height:1}
.quote{position:absolute;left:114px;top:28px;width:360px;font-family:'Montserrat',sans-serif;font-weight:600;font-size:17.5px;color:var(--brown-text);line-height:1.22}
.quote-by{position:absolute;right:40px;top:74px;font-family:'Montserrat',sans-serif;font-weight:800;font-size:15px;color:var(--green)}
.letter{position:absolute;left:29px;top:117px;width:438px;font-size:7.3px;line-height:1.3;color:#333}
.letter p{margin-bottom:8px}
.fade-scene{position:absolute;left:0;top:290px;width:493px;height:349px;background:linear-gradient(180deg,#ffffff 0%,#eceeef 40%,#d9dcde 100%)}
.ornament{position:absolute;left:210px;top:295px;width:115px;height:50px;border-radius:25px;background:radial-gradient(circle,#c8324a 0%,#7c5aa0 45%,#3a8c8c 80%,transparent 81%)}
.cta{position:absolute;left:219px;top:375px;width:260px;font-family:'Montserrat',sans-serif;font-weight:800;font-size:11.5px;color:var(--brown-text);line-height:1.15}
.cta-note{position:absolute;left:221px;font-size:8.5px;font-weight:500;color:#222}
.contact{position:absolute;left:219px;top:468px;width:290px;height:88px;background:var(--blue);border-radius:8px 0 0 8px;padding:10px 20px}
.contact .inner{border:1px dashed rgba(255,255,255,.35);position:absolute;inset:5px -10px 5px 5px;border-radius:6px}
.contact .who{font-family:'Montserrat',sans-serif;font-weight:700;font-size:18px;color:var(--green);border-bottom:1px solid rgba(255,255,255,.35);padding-bottom:3px;width:232px}
.contact .line{display:flex;align-items:center;gap:7px;color:#fff;font-size:13px;font-weight:500;margin-top:3px}

/* page 3 */
.july-band{position:absolute;left:189px;top:31px;width:304px;height:74px;background:var(--green)}
.july-word{position:absolute;left:196px;top:34px;font-family:'Anton',sans-serif;font-size:62px;color:#fff;line-height:1}
.year-box{position:absolute;left:315px;top:31px;width:178px;height:74px;background:var(--blue);border-radius:14px 0 0 14px}
.year-box .yr{position:absolute;left:12px;top:2px;font-family:'Montserrat',sans-serif;font-weight:800;font-size:34px;color:#fff}
.year-box .days{position:absolute;left:13px;top:44px;font-family:'Anton',sans-serif;font-size:20px;color:#fff;letter-spacing:.5px;word-spacing:4px}
.year-box sup{font-size:10px}
.events{position:absolute;left:33px;top:135px;width:225px}
.events h3{font-family:'Montserrat',sans-serif;font-weight:800;font-size:14px;color:var(--blue);margin-bottom:9px}
.ev{border-bottom:1px solid #bbb;padding-bottom:6px;margin-bottom:9px}
.ev h4{font-family:'Montserrat',sans-serif;font-weight:800;font-size:14px;color:var(--brown-text);line-height:1}
.ev h4.g{color:var(--green)}
.ev p,.events .foot{font-size:9.5px;line-height:1.25;color:#222}
.ev p b{color:var(--blue)}
.ev.last{border:none}
.events .foot{font-weight:600;margin-bottom:7px}
.blue-card{position:absolute;left:290px;top:127px;width:176px;height:247px;background:var(--blue);border-radius:14px;padding:26px 12px 0 12px;color:#fff;font-size:9.1px;line-height:1.2}
.blue-card .over{font-size:14px;margin-top:6px}
.thirty{display:flex;align-items:center;margin:-2px 0 4px -2px}
.thirty .n{font-family:'Anton',sans-serif;font-size:48px;color:var(--green);line-height:1}
.thirty .pill{background:var(--green);color:var(--blue);font-family:'Montserrat',sans-serif;font-weight:800;font-size:20px;padding:2px 14px 2px 8px;border-radius:0 16px 16px 0;margin-left:2px}
.info{position:absolute;left:286px;top:405px;width:180px}
.info h3{font-family:'Montserrat',sans-serif;font-weight:800;font-size:14px;color:var(--blue);line-height:1.1}
.info h4{font-family:'Montserrat',sans-serif;font-weight:800;color:var(--brown-text);font-size:13px;line-height:1}
.info h4.big{font-size:18px}
.info .band{font-family:'Montserrat',sans-serif;font-weight:800;font-size:10px;margin:3px 0 11px}
.info .lead{font-weight:600;font-size:9px;line-height:1.2}
.info .small{font-size:7.8px;color:#333;line-height:1.25;margin-top:3px}

/* package cards */
.card{position:absolute;background:var(--pale);border-radius:8px;overflow:hidden}
.cap{position:absolute;left:50%;transform:translateX(-50%);top:0;width:108px;height:52px;border-radius:0 0 54px 54px;color:#fff;text-align:center;font-family:'Montserrat',sans-serif;font-weight:800;font-size:11.5px;line-height:1;padding-top:14px}
.cap.dark{color:#2b2b2b}
.cap-blue{background:linear-gradient(180deg,#3c9ad1,#1c6aa3)}
.cap-bronze{background:linear-gradient(180deg,#d39a4c,#8b5219)}
.cap-silver{background:linear-gradient(180deg,#f4f4f4,#9b9b9b)}
.cap-gold{background:linear-gradient(180deg,#f2d35b,#b48a0c)}
.cap-plat{background:linear-gradient(180deg,#f6f6f6,#a2a2a2)}
.cap-saloon{background:linear-gradient(180deg,#c8e660,#7fae1d)}
.cap-orange{background:linear-gradient(180deg,#f7b13b,#e4841b)}
.cap-red{background:linear-gradient(180deg,#f24b3c,#c9170f)}
.perks{position:absolute;left:12px;right:8px;list-style:none;font-size:7px;line-height:1.22;color:#222}
.perks li{position:relative;padding-left:10px;margin-bottom:7px}
.perks.tight li{margin-bottom:1px}
.perks li::before{content:"";position:absolute;left:0;top:2.5px;width:4px;height:4px;border-radius:50%;background:var(--green)}
.perks li.plain{padding-left:10px}
.perks li.plain::before{display:none}
.rule{position:absolute;left:8px;right:8px;height:1px;background:#b9c4cc}
.tix{position:absolute;left:10px;display:flex;align-items:center;gap:6px;font-size:7.5px;line-height:1.15;color:#222}
.note{position:absolute;left:10px;right:8px;font-size:7.5px;line-height:1.15;color:#222}

/* page 5 */
.land{position:absolute;left:0;top:460px;width:493px;height:179px;background:linear-gradient(180deg,#ffffff 0%,#dad9d3 30%,#a9a795 65%,#8d8b7a 100%)}
.steak-tab{position:absolute;left:0;top:25px;width:52px;height:104px;border-radius:0 52px 52px 0;background:#2a2a2a;color:#fff}
.steak-tab span{position:absolute;left:8px;top:74px;transform:rotate(-90deg);transform-origin:left top;font-family:'Montserrat',sans-serif;font-weight:800;font-size:11px;line-height:1;width:70px;text-align:center}

/* page 6 */
.invoice-title{position:absolute;left:29px;top:108px;font-family:'Montserrat',sans-serif;font-weight:800;font-size:30px;color:var(--blue)}
.bill{position:absolute;left:172px;top:31px;width:321px;height:104px;background:var(--brown-text);border-radius:8px 0 0 8px;padding:10px 28px 0 17px}
.bill .row{display:flex;border-bottom:1px dashed rgba(255,255,255,.35);padding:3px 0 2px;font-size:7.5px;color:#fff}
.bill .row .k{width:89px;color:#f2a743;font-weight:600}
.invoice{position:absolute;left:29px;top:178px;width:438px;border-collapse:separate;border-spacing:4px 4px;margin-left:-4px;font-size:8.5px}
.invoice th{background:#2b2b2b;color:#fff;font-weight:500;height:18px;font-size:9px}
.invoice th.first{background:var(--green);text-align:left;padding-left:9px;width:212px}
.invoice td{background:#eceeef;height:20px;padding-left:11px;color:#222}
.invoice td.c{text-align:center;padding:0}
.invoice-foot{position:absolute;left:0;top:453px;width:493px;height:186px;background:var(--blue)}
.pay{position:absolute;left:29px;top:417px;display:flex;gap:4px}
.pay div{background:#eceeef;height:75px}
</style>
</head>
<body>

<!-- Page: cover -->
<section class="page" style="left:84px;top:131px">
  <div class="brand" style="left:176px;top:40px">
    <span class="dot"></span>
    <span><span class="name">FENWICK CREEK</span><br><span class="sub">FIRST NATION<br>CREEK WATER PEOPLE</span></span>
  </div>
  <div class="cover-band"></div>
  <svg class="abs" style="left:60px;top:120px" width="360" height="350" viewBox="0 0 360 350">
    <path d="M 60 310 A 172 172 0 0 1 120 20" fill="none" stroke="#8cb526" stroke-width="9"/>
    <path d="M 110 30 A 172 172 0 0 1 330 270" fill="none" stroke="#1d5a86" stroke-width="11"/>
    <path d="M 330 270 A 172 172 0 0 1 60 310" fill="none" stroke="#8cb526" stroke-width="7"/>
    <circle cx="186" cy="172" r="150" fill="#ffffff"/>
  </svg>
  <div class="photo" role="img" aria-label="Photo: a bronc rider on a bucking paint horse in the rodeo arena" style="left:103px;top:150px;width:286px;height:286px;border-radius:50%;background:radial-gradient(circle at 55% 45%,#8a5a38 0%,#6d7f7c 45%,#4e6a72 100%)"></div>
  <h1 class="cover-title">RODEO SPONSORSHIP</h1>
  <div class="cover-sub">PROPOSAL</div>
  <div class="url cover-url">www.<b>fenwickcreekfn</b>.com</div>
</section>

<!-- Page: letter -->
<section class="page" style="left:622px;top:131px">
  <div class="quote-ghost">&rdquo;</div>
  <div class="quote-mark">&ldquo;</div>
  <blockquote class="quote">&ldquo;Courage is being scared to death and saddling up anyway!&rdquo;</blockquote>
  <div class="quote-by">– HANK TOLLIVER</div>
  <div class="letter">
    <p>2 One day Rodeos with amazing prizes and buckles each day with the average winning a FCFN Drum! The Fenwick Creek Rodeo is an attraction to many local cowboys and cowgirls from local communities, Fort St. John and across BC, AB and surrounding areas. We offer youth to adult events that are all crowd pleasers. Since the beginning this has been an annual event up until Covid-19 when we have had to take a break but we are so excited to build it bigger and better then before!</p>
    <p>We have some big plans for the future of the Fenwick Creek Rodeo including an expansion of the Rodeo grounds, new event buildings, new office/announcer booths as well as the purchase of new grandstands. This will be a big endeavor that we think will benefit both our community as well as the local community.</p>
    <p>Our rodeo would not have flourished without the support and generosity we have received from your sponsorship over the years. Once again, we are hoping your company will give generously to our yearly event and help continue to make our rodeo a success. All support goes towards any supplies not covered by donation, the purchase of materials to upgrade the rodeo grounds, rodeo stock and event payout. We hope to attract even more rodeo events, larger entertainers, and more fans through the gates. Your sponsorship will be highly regarded for what we hope will be generations to come.</p>
  </div>
  <div class="fade-scene" role="img" aria-label="Faded photo of rodeo spectators in the grandstand"></div>
  <div class="photo" role="img" aria-label="Photo: a cowboy in a blue plaid shirt riding a bucking bronc" style="left:10px;top:285px;width:200px;height:354px;background:linear-gradient(180deg,#3e6fa8 0%,#5b3a22 55%,#3a2a1e 100%);border-radius:40% 40% 0 0"></div>
  <div class="ornament" role="img" aria-label="Beadwork floral ornament"></div>
  <div class="cta">PLEASE SEE THE LEVEL OF SPONSORSHIP ATTACHED, FILL AND RETURN TO THE FENWICK CREEK RODEO!</div>
  <div class="cta-note" style="top:428px">Your sponsorship is greatly appreciated.</div>
  <div class="cta-note" style="top:449px">For further information please call or email</div>
  <div class="contact">
    <div class="inner"></div>
    <div class="who">Marla Dunning</div>
    <div class="line"><svg width="11" height="11" viewBox="0 0 24 24"><path fill="#8cb526" d="M6.6 10.8a15 15 0 0 0 6.6 6.6l2.2-2.2c.3-.3.7-.4 1-.2 1.1.4 2.3.6 3.6.6.6 0 1 .4 1 1V20c0 .6-.4 1-1 1A17 17 0 0 1 3 4c0-.6.4-1 1-1h3.5c.6 0 1 .4 1 1 0 1.3.2 2.5.6 3.6.1.3 0 .7-.2 1z"/></svg>250.555.0142</div>
    <div class="line"><svg width="11" height="9" viewBox="0 0 22 16"><rect x="1" y="1" width="20" height="14" fill="none" stroke="#8cb526" stroke-width="2"/><path d="M1 1l10 8 10-8" fill="none" stroke="#8cb526" stroke-width="2"/></svg>mdunning@fenwickcreekfn.com</div>
  </div>
  <div class="url" style="left:301px;top:592px"><b>www.fenwickcreekfn.com</b><span class="pnum">1</span></div>
</section>

<!-- Page: dates -->
<section class="page" style="left:84px;top:825px">
  <h2 class="section" style="left:30px;top:30px;font-size:40px"><span class="top">RODEO</span><span class="bot">DATES</span></h2>
  <div class="july-band"></div>
  <div class="july-word">JULY</div>
  <div class="year-box"><div class="yr">2023</div><div class="days">28<sup>TH</sup> 29<sup>TH</sup> 30<sup>TH</sup></div></div>
  <div class="events">
    <h3>EVENTS</h3>
    <div class="ev"><h4>JULY 28</h4><p>Gymkhana and family Dance</p></div>
    <div class="ev"><h4 class="g">JULY 29</h4><p>Junior Rodeo at <b>11 am</b>, Main Rodeo starts at <b>2pm</b> with Steak Dinner and Rodeo dance to follow Band is The Dusty Meridians</p></div>
    <div class="ev last"><h4>JULY 30</h4><p>Junior Rodeo at <b>11 am</b>,<br>Main Rodeo starts at <b>2pm</b></p></div>
    <p class="foot">Free Pancake Breakfast<br>both Saturday and Sunday Morning</p>
    <p class="foot">Cultural Events happening<br>throughout the day.</p>
  </div>
  <div class="blue-card">
    <p>Saddle up for the Fenwick Creek Rodeo held at the Fenwick Creek First Nation Rodeo grounds! This is now a 3 day family fun event with the addition of a Friday afternoon Gymkhana!</p>
    <p style="margin-top:8px">Fenwick Creek Rodeo has been running for</p>
    <p class="over">OVER</p>
    <div class="thirty"><span class="n">30</span><span class="pill">YEARS</span></div>
    <p>and we are exciting to bring the excitement back.</p>
  </div>
  <div class="abs" role="img" aria-label="Beadwork floral ornament" style="left:322px;top:358px;width:115px;height:46px;border-radius:23px;background:radial-gradient(circle,#c8324a 0%,#7c5aa0 45%,#3a8c8c 80%,transparent 81%)"></div>
  <div class="photo" role="img" aria-label="Photo: elders in cowboy hats singing with hand drums" style="left:28px;top:405px;width:238px;height:185px;border-radius:10px;background:linear-gradient(160deg,#1a1a1a 0%,#4a3a2c 45%,#b9a78e 100%)"></div>
  <div class="info">
    <h3>INFORMATION</h3>
    <h4>DANCE</h4>
    <h4 class="big">JULY 29</h4>
    <p class="band">THE DUSTY MERIDIANS</p>
    <p class="lead">Share you companies<br>Value:</p>
    <p class="small">Have a look and let us know how we can help you connect with the right network for you.</p>
  </div>
  <div class="url" style="left:303px;top:603px"><b>www.fenwickcreekfn.com</b><span class="pnum">2</span></div>
</section>

<!-- Page: packages -->
<section class="page" style="left:622px;top:825px">
  <h2 class="section" style="left:0;width:493px;text-align:center;top:32px;font-size:37px"><span class="top">RODEO</span><span class="bot">PACKAGES</span></h2>

  <div class="card" style="left:30px;top:124px;width:139px;height:173px">
    <div class="cap cap-blue">STARTER<br>PACKAGE</div>
    <ul class="perks" style="top:62px"><li>Company logo on the big screen</li><li>Company logo on Web and program</li></ul>
    <div class="rule" style="top:116px"></div>
    <div class="tix" style="top:130px"><svg width="50" height="26" viewBox="0 0 50 26"><rect x="3" y="4" width="44" height="18" rx="2" fill="#fff" stroke="#1d5a86" stroke-width="2" transform="rotate(-8 25 13)"/><text x="8" y="18" font-size="7" fill="#1d5a86" font-family="serif" transform="rotate(-8 25 13)">TICKET</text></svg><span>2 admission<br>tickets to<br>Sunday rodeo</span></div>
  </div>
  <div class="card" style="left:177px;top:124px;width:139px;height:173px">
    <div class="cap cap-bronze">BRONZE<br>PACKAGE</div>
    <ul class="perks" style="top:62px"><li>Social media Ads and mentions</li><li>Company logo on Big screen</li><li>Company logo on Web</li></ul>
    <div class="rule" style="top:116px"></div>
    <div class="tix" style="top:130px"><svg width="50" height="26" viewBox="0 0 50 26"><rect x="3" y="4" width="44" height="18" rx="2" fill="#fff" stroke="#1d5a86" stroke-width="2" transform="rotate(-8 25 13)"/><text x="8" y="18" font-size="7" fill="#1d5a86" font-family="serif" transform="rotate(-8 25 13)">TICKET</text></svg><span>4 admission<br>tickets to<br>Sunday rodeo</span></div>
  </div>
  <div class="card" style="left:324px;top:124px;width:139px;height:173px">
    <div class="cap cap-silver dark">SILVER<br>PACKAGE</div>
    <ul class="perks" style="top:56px"><li>Social media Ads and mentions</li><li>Company logo on Big screen</li><li>Company logo on Web Banner (sponsor provided) in arena</li></ul>
    <div class="rule" style="top:116px"></div>
    <div class="tix" style="top:130px"><svg width="50" height="26" viewBox="0 0 50 26"><rect x="3" y="4" width="44" height="18" rx="2" fill="#fff" stroke="#1d5a86" stroke-width="2" transform="rotate(-8 25 13)"/><text x="8" y="18" font-size="7" fill="#1d5a86" font-family="serif" transform="rotate(-8 25 13)">TICKET</text></svg><span>4 weekend<br>passes</span></div>
  </div>

  <div class="card" style="left:30px;top:316px;width:139px;height:247px">
    <div class="cap cap-gold">GOLD<br>PACKAGE</div>
    <ul class="perks" style="top:62px"><li>Social media Ads and mentions</li><li>Company logo on Big screen</li><li class="plain">Company logo on Web</li><li class="plain">Banner (sponsor provided) in arena</li></ul>
    <div class="rule" style="top:174px"></div>
    <div class="tix" style="top:178px"><svg width="50" height="26" viewBox="0 0 50 26"><rect x="3" y="4" width="44" height="18" rx="2" fill="#fff" stroke="#1d5a86" stroke-width="2" transform="rotate(-8 25 13)"/><text x="8" y="18" font-size="7" fill="#1d5a86" font-family="serif" transform="rotate(-8 25 13)">TICKET</text></svg><span>6 weekend<br>passes</span></div>
    <p class="note" style="top:213px">6 Dance tickets (must be age of majority) including steak dinner</p>
  </div>
  <div class="card" style="left:177px;top:316px;width:139px;height:247px">
    <div class="cap cap-plat dark">PLATINUM<br>PACKAGE</div>
    <ul class="perks tight" style="top:62px"><li>Pre event Radio advertising Company logo on posters</li><li>Social media Ads and mentions</li><li>Company logo on Big screen</li><li>Company logo on Web</li><li>Commercial on the big screen</li><li>2 large Banners (sponsor provided) in arena</li></ul>
    <div class="rule" style="top:174px"></div>
    <div class="tix" style="top:178px"><svg width="50" height="26" viewBox="0 0 50 26"><rect x="3" y="4" width="44" height="18" rx="2" fill="#fff" stroke="#1d5a86" stroke-width="2" transform="rotate(-8 25 13)"/><text x="8" y="18" font-size="7" fill="#1d5a86" font-family="serif" transform="rotate(-8 25 13)">TICKET</text></svg><span>8 weekend<br>passes</span></div>
    <p class="note" style="top:213px">8 Dance tickets (must be age of majority) including steak dinner</p>
  </div>
  <div class="card" style="left:324px;top:316px;width:139px;height:247px">
    <div class="cap cap-saloon">SALOON<br>PACKAGE</div>
    <ul class="perks tight" style="top:62px"><li>Pre event Radio advertising</li><li>Company logo on posters</li><li>Social media Ads and mentions</li><li>Company logo on Big screen</li><li>Company logo on Web</li><li>Commercial on the big screen</li><li>2 large Banners (sponsor provided) in arena</li></ul>
    <div class="rule" style="top:174px"></div>
    <div class="tix" style="top:178px"><svg width="50" height="26" viewBox="0 0 50 26"><rect x="3" y="4" width="44" height="18" rx="2" fill="#fff" stroke="#1d5a86" stroke-width="2" transform="rotate(-8 25 13)"/><text x="8" y="18" font-size="7" fill="#1d5a86" font-family="serif" transform="rotate(-8 25 13)">TICKET</text></svg><span>6 weekend<br>passes</span></div>
    <p class="note" style="top:213px">6 Dance tickets (must be age of majority) including steak dinner</p>
  </div>
  <div class="url" style="left:297px;top:603px"><b>www.fenwickcreekfn.com</b><span class="pnum">3</span></div>
</section>

<!-- Page: more packages -->
<section class="page" style="left:84px;top:1519px">
  <div class="land" role="img" aria-label="Photo: misty river valley landscape with a fence post"></div>
  <h2 class="section" style="left:0;width:493px;text-align:center;top:32px;font-size:37px"><span class="top">RODEO</span><span class="bot">PACKAGES</span></h2>

  <div class="card" style="left:46px;top:115px;width:198px;height:175px">
    <div class="cap cap-orange" style="width:104px;height:56px;padding-top:10px;font-size:11px">PANCAKE<br>BREAKFAST<br>PACKAGE</div>
    <p class="abs" style="left:13px;top:65px;font-size:7px;font-weight:700">2 MORNINGS</p>
    <ul class="perks" style="top:79px;font-size:8px"><li style="margin-bottom:6px">Social media Ads and mentions</li><li style="margin-bottom:6px">Company logo on Big screen</li><li>Company logo on Web</li></ul>
    <div class="rule" style="top:122px"></div>
    <div class="tix" style="top:135px;left:38px"><svg width="54" height="28" viewBox="0 0 50 26"><rect x="3" y="4" width="44" height="18" rx="2" fill="#fff" stroke="#1d5a86" stroke-width="2" transform="rotate(-8 25 13)"/><text x="8" y="18" font-size="7" fill="#1d5a86" font-family="serif" transform="rotate(-8 25 13)">TICKET</text></svg><span>4 weekend<br>passes</span></div>
  </div>
  <div class="card" style="left:251px;top:115px;width:198px;height:175px">
    <div class="cap cap-red" style="width:104px;height:52px">KIDS FUN<br>PACKAGE</div>
    <ul class="perks" style="top:67px;font-size:8px"><li style="margin-bottom:6px">Company logo on the big screen</li><li style="margin-bottom:6px">Company logo on Web and program</li><li>Social Media Ads and Mentions</li></ul>
    <div class="rule" style="top:122px"></div>
    <div class="tix" style="top:135px;left:38px"><svg width="54" height="28" viewBox="0 0 50 26"><rect x="3" y="4" width="44" height="18" rx="2" fill="#fff" stroke="#1d5a86" stroke-width="2" transform="rotate(-8 25 13)"/><text x="8" y="18" font-size="7" fill="#1d5a86" font-family="serif" transform="rotate(-8 25 13)">TICKET</text></svg><span>2 weekend<br>passes</span></div>
  </div>

  <div class="card" style="left:46px;top:300px;width:403px;height:150px">
    <div class="steak-tab"><span>STEAK<br>DINNER</span></div>
    <ul class="perks" style="left:76px;right:auto;width:160px;top:18px;font-size:7.8px"><li style="margin-bottom:4px">Pre event Radio advertising</li><li style="margin-bottom:4px">Company logo on posters</li><li style="margin-bottom:4px">Social media Ads and mentions</li><li style="margin-bottom:4px">Company logo on Big screen</li><li style="margin-bottom:4px">Company logo on Web</li><li style="margin-bottom:4px">Commercial on the big screen</li><li>2 large Banners (sponsor provided) in arena</li></ul>
    <div class="abs" style="left:234px;top:10px;width:1px;height:130px;background:#1d5a86"></div>
    <svg class="abs" style="left:258px;top:22px" width="120" height="60" viewBox="0 0 120 60"><g transform="rotate(-14 60 30)"><rect x="6" y="12" width="108" height="36" rx="3" fill="#fff" stroke="#1d5a86" stroke-width="3"/><line x1="88" y1="12" x2="88" y2="48" stroke="#1d5a86" stroke-width="2" stroke-dasharray="3 3"/><text x="16" y="38" font-size="15" fill="#1d5a86" font-family="serif">TICKET</text></g></svg>
    <p class="abs" style="left:278px;top:95px;font-size:7.8px">6 weekend passes</p>
    <p class="abs" style="left:248px;top:110px;width:150px;font-size:7.8px;line-height:1.15;text-align:center">6 Dance tickets (must be age of majority) including steak dinner</p>
  </div>
  <div class="url" style="left:24px;top:605px"><span class="pnum" style="margin:0 6px 0 0">4</span><b>www.fenwickcreekfn.com</b></div>
</section>

<!-- Page: invoice -->
<section class="page" style="left:622px;top:1519px">
  <div class="brand" style="left:29px;top:38px">
    <span class="dot"></span>
    <span><span class="name">FENWICK CREEK</span><br><span class="sub">FIRST NATION<br>CREEK WATER PEOPLE</span></span>
  </div>
  <h2 class="invoice-title">INVOICE</h2>
  <div class="bill">
    <div class="row"><span class="k">Company Name</span><span>Fenwick Creek FN</span></div>
    <div class="row"><span class="k">Address</span><span>P.O. Box 48<br>Aspen Flats, BC V0C 1X0</span></div>
    <div class="row"><span class="k">Phone Number</span><span>250-555-0187</span></div>
    <div class="row" style="border:none"><span class="k">Email</span><span>accounts@fenwickcreekfn.com</span></div>
  </div>
  <div class="invoice-foot"></div>
  <table class="invoice">
    <thead><tr><th class="first">Rodeo Packages</th><th>Quantity</th><th>Cost</th><th>Total</th></tr></thead>
    <tbody>
      <tr><td>Starter Package</td><td></td><td class="c">$750</td><td></td></tr>
      <tr><td>Bronze Package</td><td></td><td class="c">$1500</td><td></td></tr>
      <tr><td>Silver Package</td><td></td><td class="c">$3000</td><td></td></tr>
      <tr><td>Gold Package</td><td></td><td class="c">$5000</td><td></td></tr>
      <tr><td>Platinum Package</td><td></td><td class="c">$7500</td><td></td></tr>
      <tr><td>Kids Fun Package</td><td></td><td class="c">$1000</td><td></td></tr>
      <tr><td>Dance saloon Package</td><td></td><td class="c">$6000</td><td></td></tr>
      <tr><td>Steak Dinner Package</td><td></td><td class="c">$4000</td><td></td></tr>
      <tr><td>Pancake Breakfast Package</td><td></td><td class="c">$2000</td><td></td></tr>
    </tbody>
  </table>
  <div class="pay">
    <div style="width:214px;padding:6px 11px;font-size:8.5px;line-height:1.2">Paid By Cheque<br><span style="font-weight:600;font-size:11.5px;color:#2b2b2b">FENWICK CREEK FIRST NATION</span><br><span style="font-size:6.5px">MEMO: RODEO</span></div>
    <div style="width:70px"></div>
    <div style="width:70px;padding:6px 7px;font-size:6.5px;line-height:1.2">TOTAL<br>INVOICE</div>
    <div style="width:70px"></div>
  </div>
  <div class="url" style="left:0;width:493px;text-align:center;top:590px;color:#fff;font-size:12px">www.<b>fenwickcreekfn</b>.com</div>
</section>

</body>
</html>
```